HOME IMPROVEMENT Business Card

I want a very unique business card. nothing typical and boring. Im open to you ideas. Ive seen cards with gold and silver or color foil and spot UV coatings. Im looking for something that looks cool and grabs attention. I like rounded corners but am open to all suggestions. We are a home improvement company and I will have a presentation folder printed and a catalog printed also and want to keep that same theme. I love the colors in our logo but I am open at looking at a 3rd color that would work with my logo. I hope that helps.
Card should include
Address
Phone
Fax
Email
Website
Target Market(s)
Home owners, people looking to remodel their home
Industry/Entity Type
Home Improvement
Contact Information for Business Card
2873 Maple Crest Avenue Unit 410
Harrowfield, Il 60284
Phone
Direct Line
Email
Website
Font styles to use
Other font styles liked:
- IM OPEN MINDED
Requirements
Must have
- High end quality look nothing boring I like rounded corners but am open minded
Nice to have
- WOW. I want something nice and impressive.
Should not have
- ??? Not sure

```html
<!DOCTYPE html>
<html lang="en">
<head>
<meta charset="utf-8">
<title>Keystead Home Remodeling Group – Business Card</title>
<link rel="stylesheet" href="https://fonts.googleapis.com/css2?family=Montserrat:wght@700;800&family=Open+Sans:wght@400&display=swap">
<style>
  :root {
    --backdrop: #c8c9cb;
    --card-white: #ffffff;
    --ink-navy: #1c2550;
    --blue-deep: #1d5fa8;
    --blue-mid: #2b78c2;
    --blue-violet: #3b4a86;
    --text-light: #ffffff;
  }
  html, body {
    margin: 0;
    padding: 0;
    width: 1200px;
    height: 1000px;
    overflow: hidden;
    background: var(--backdrop);
  }
  .canvas {
    position: relative;
    width: 1200px;
    height: 1000px;
  }
  .card {
    position: absolute;
    width: 560px;
    height: 320px;
    border-radius: 4px;
    overflow: hidden;
  }
  .card-front {
    left: 110px;
    top: 110px;
    background: var(--card-white);
    display: flex;
    align-items: center;
    justify-content: center;
  }
  .brand {
    text-align: left;
    color: var(--ink-navy);
  }
  .brand-name {
    display: flex;
    align-items: center;
    gap: 14px;
    font-family: "Montserrat", sans-serif;
    font-weight: 800;
    font-size: 64px;
    line-height: 1;
    letter-spacing: -1px;
  }
  .brand-mark {
    width: 22px;
    height: 22px;
    background: var(--ink-navy);
  }
  .brand-tagline {
    margin-top: 8px;
    font-family: "Montserrat", sans-serif;
    font-weight: 700;
    font-size: 15px;
    letter-spacing: 5.4px;
  }
  .card-back {
    left: 530px;
    top: 570px;
  }
  .back-field {
    position: absolute;
    inset: 0;
    background: linear-gradient(100deg, var(--blue-mid) 0%, var(--blue-deep) 50%, var(--blue-violet) 100%);
  }
  .contact {
    position: absolute;
    left: 0;
    top: 126px;
    margin: 0;
    display: grid;
    grid-template-columns: 120px auto;
    column-gap: 8px;
    row-gap: 6px;
    font-family: "Open Sans", sans-serif;
    font-size: 14px;
    color: var(--text-light);
  }
  .contact dt { text-align: right; }
  .contact dd { margin: 0; white-space: nowrap; }
</style>
</head>
<body>
<main class="canvas">
  <section class="card card-front" aria-label="Business card front">
    <div class="brand">
      <div class="brand-name"><span class="brand-mark"></span>Keystead</div>
      <div class="brand-tagline">HOME REMODELING GROUP</div>
    </div>
  </section>

  <section class="card card-back" aria-label="Business card back">
    <div class="back-field" role="img" aria-label="Blue abstract background of overlapping curved shapes"></div>
    <dl class="contact">
      <dt>Address :</dt><dd>2873 Maple Crest Avenue Unit 410, Harrowfield, Il 60284</dd>
      <dt>Phone :</dt><dd>+123 456 789</dd>
      <dt>Fax :</dt><dd>+123 456 789</dd>
      <dt>Email :</dt><dd>name@mail.com</dd>
      <dt>Website :</dt><dd>https://website.com</dd>
    </dl>
  </section>
</main>
</body>
</html>
```